Brindlequest.com is a mountain biking and climbing travel company. We need a advertisement fo...

We need a advertisement for the back cover of a guide book. We would like a simple but strong ad that includes our logo. It must state that we are a biking and climbing company and people can contact us at the web site brindlequest.com We would like you to incorparate and below photo and logo on the ad.

```html
<!DOCTYPE html>
<html lang="en">
<head>
<meta charset="utf-8">
<title>Brindlequest Tours – Climbing &amp; Riding</title>
<link rel="stylesheet" href="https://fonts.googleapis.com/css2?family=Michroma&family=Poppins:wght@400;500;600;800&display=swap">
<style>
  :root {
    --backdrop: #9a9a9a;
    --paper: #ffffff;
    --ink: #222222;
    --accent: #e8a22a;
    --night: #121212;
    --text-light: #ffffff;
  }
  * { box-sizing: border-box; margin: 0; padding: 0; }
  html, body { width: 1200px; height: 1200px; overflow: hidden; }
  body {
    background: var(--backdrop);
    font-family: "Poppins", sans-serif;
    position: relative;
  }
  .flyer {
    position: absolute;
    left: 218px; top: 58px;
    width: 764px; height: 1082px;
    background: var(--paper);
    overflow: hidden;
  }
  .street-photo {
    position: absolute;
    left: 0; top: 0; width: 764px; height: 1036px;
    background:
      linear-gradient(180deg, rgba(255,255,255,1) 0%, rgba(255,255,255,0.75) 14%, rgba(255,255,255,0) 30%),
      radial-gradient(ellipse 120px 160px at 48% 42%, rgba(248,190,80,0.85), rgba(248,190,80,0) 100%),
      linear-gradient(90deg, #c99a86 0%, #b8907a 22%, #7a6450 42%, #8b7a62 55%, #e6e2dc 72%, #f1efea 100%),
      #8a7a6a;
  }
  .street-photo::after {
    content: "";
    position: absolute; inset: 0;
    background: linear-gradient(180deg, rgba(0,0,0,0) 45%, rgba(70,70,70,0.55) 62%, rgba(20,20,20,0.92) 80%, var(--night) 92%);
  }
  .title-frame {
    position: absolute;
    left: 62px; top: 43px; width: 645px; height: 191px;
    border: 3px solid var(--ink);
  }
  .title {
    position: absolute;
    left: 0; top: 58px; width: 764px;
    text-align: center;
    font-family: "Michroma", sans-serif;
    color: var(--ink);
    line-height: 1.12;
  }
  .title .line-one { display: block; font-size: 44px; letter-spacing: 1px; }
  .title .line-two { display: block; font-size: 54px; letter-spacing: 1px; }
  .tagline-band {
    position: absolute;
    left: 100px; top: 193px; width: 565px; height: 75px;
    background: var(--accent);
    color: var(--text-light);
    font-weight: 800;
    font-size: 50px;
    line-height: 75px;
    text-align: center;
    letter-spacing: -0.5px;
  }
  .brand-mark {
    position: absolute;
    left: 0; top: 820px; width: 764px;
    display: flex; align-items: center; justify-content: center; gap: 18px;
    color: var(--text-light);
    font-weight: 600;
    font-size: 50px;
    letter-spacing: 1px;
  }
  .brand-mark .dot {
    width: 46px; height: 46px; border-radius: 50%;
    background: var(--text-light);
  }
  .contact-phone {
    position: absolute; left: 0; top: 926px; width: 764px;
    display: flex; align-items: center; justify-content: center; gap: 12px;
    color: var(--accent);
    font-weight: 600; font-size: 30px;
  }
  .address {
    position: absolute; left: 0; width: 764px;
    display: flex; align-items: center; justify-content: center; gap: 7px;
    color: var(--text-light);
    font-weight: 500; font-size: 14.5px;
  }
  .address.swiss { top: 974px; }
  .address.perth { top: 1001px; }
  .web-footer {
    position: absolute; left: 0; top: 1036px; width: 764px; height: 46px;
    background: var(--paper);
    text-align: center;
    line-height: 46px;
    font-size: 15px;
    letter-spacing: 6px;
    color: var(--ink);
  }
</style>
</head>
<body>
  <main class="flyer">
    <div class="street-photo" role="img" aria-label="Evening photo of a narrow cobbled old-town street with warm lit shops and a motion-blurred cyclist riding past"></div>

    <div class="title-frame"></div>
    <h1 class="title">
      <span class="line-one">BRINDLEQUEST</span>
      <span class="line-two">TOURS</span>
    </h1>
    <div class="tagline-band">CLIMBING &amp; RIDNG</div>

    <div class="brand-mark"><span class="dot"></span><span>BRINDLEQUEST</span></div>

    <div class="contact-phone">
      <svg width="26" height="26" viewBox="0 0 24 24" aria-hidden="true">
        <path fill="var(--accent)" d="M6.6 10.8a15.1 15.1 0 0 0 6.6 6.6l2.2-2.2a1 1 0 0 1 1-.25 11.4 11.4 0 0 0 3.6.57 1 1 0 0 1 1 1V20a1 1 0 0 1-1 1A17 17 0 0 1 3 4a1 1 0 0 1 1-1h3.5a1 1 0 0 1 1 1c0 1.25.2 2.45.57 3.57a1 1 0 0 1-.25 1z"/>
      </svg>
      <span>Call Us Today : +41 79 555 0142</span>
    </div>

    <div class="address swiss">
      <svg width="14" height="18" viewBox="0 0 24 30" aria-hidden="true"><path fill="var(--accent)" d="M12 0a11 11 0 0 0-11 11c0 8 11 19 11 19s11-11 11-19A11 11 0 0 0 12 0zm0 15.5A4.5 4.5 0 1 1 12 6.5a4.5 4.5 0 0 1 0 9z"/></svg>
      <span>RUE DES PINS 12, AUBONNE, SWITZERLAND</span>
    </div>
    <div class="address perth">
      <svg width="14" height="18" viewBox="0 0 24 30" aria-hidden="true"><path fill="var(--accent)" d="M12 0a11 11 0 0 0-11 11c0 8 11 19 11 19s11-11 11-19A11 11 0 0 0 12 0zm0 15.5A4.5 4.5 0 1 1 12 6.5a4.5 4.5 0 0 1 0 9z"/></svg>
      <span>14 MARLOW STREET, SCARBOROUGH, PERTH, WESTERN AUSTRALIA</span>
    </div>

    <footer class="web-footer">www.brindlequest.com</footer>
  </main>
</body>
</html>
```